Cover for Inspirational Daily Journal

This is the cover for a daily journal that will focus on inspirational content for black women. The cover should have a picture or silhouette of a black woman with a crown. The title is: "Grace in Bloom: A Year of Bright Mornings." The back won't have any words. Also the journal will be published on Pagewick.

```html
<!DOCTYPE html>
<html lang="en">
<head>
<meta charset="utf-8">
<title>Grace in Bloom – Journal Cover</title>
<link rel="stylesheet" href="https://fonts.googleapis.com/css2?family=DM+Serif+Display&family=Montserrat:wght@400;500&display=swap">
<style>
  :root {
    --backdrop: #6a6a6a;
    --cover-purple: #3a1745;
    --cover-purple-deep: #2b1033;
    --spine-purple: #2a0f31;
    --gold: #e0b850;
    --spine-text: #8c7a90;
    --figure-dark: #141414;
    --figure-mid: #241a26;
  }
  * { margin: 0; padding: 0; box-sizing: border-box; }
  html, body {
    width: 1200px;
    height: 800px;
    overflow: hidden;
    background: var(--backdrop);
  }
  .canvas {
    position: relative;
    width: 1200px;
    height: 800px;
  }
  .book {
    position: absolute;
    left: 355px;
    top: 50px;
    width: 490px;
    height: 700px;
    display: flex;
    box-shadow: 0 12px 30px rgba(0,0,0,0.35);
  }
  .spine {
    width: 40px;
    height: 100%;
    background: linear-gradient(90deg, var(--spine-purple), var(--cover-purple-deep));
    display: flex;
    justify-content: center;
    padding-top: 60px;
  }
  .spine-publisher {
    writing-mode: vertical-rl;
    font-family: "Montserrat", sans-serif;
    font-weight: 400;
    font-size: 15px;
    letter-spacing: 1.5px;
    color: var(--spine-text);
  }
  .front-cover {
    position: relative;
    flex: 1;
    height: 100%;
    overflow: hidden;
    background: radial-gradient(ellipse at 60% 55%, #4a1d5a 0%, var(--cover-purple) 45%, var(--cover-purple-deep) 100%);
  }
  .cover-title {
    position: absolute;
    top: 60px;
    left: 0;
    right: 0;
    text-align: center;
    font-family: "DM Serif Display", serif;
    font-weight: 400;
    font-size: 66px;
    line-height: 0.95;
    color: var(--gold);
  }
  .cover-subtitle {
    position: absolute;
    top: 222px;
    left: 0;
    right: 0;
    text-align: center;
    font-family: "Montserrat", sans-serif;
    font-weight: 500;
    font-size: 14px;
    letter-spacing: 2px;
    color: var(--gold);
  }
  .crowned-figure {
    position: absolute;
    left: 90px;
    right: 40px;
    top: 275px;
    bottom: 0;
    border-radius: 140px 140px 0 0;
    background: linear-gradient(180deg, #b8953f 0%, var(--figure-mid) 28%, var(--figure-dark) 100%);
  }
</style>
</head>
<body>
  <main class="canvas">
    <section class="book">
      <div class="spine">
        <span class="spine-publisher">Ardenne &amp; Co.</span>
      </div>
      <div class="front-cover">
        <h1 class="cover-title">Grace in<br>Bloom</h1>
        <p class="cover-subtitle">A YEAR OF BRIGHT MORNINGS</p>
        <div class="crowned-figure" role="img" aria-label="Silhouette of a Black woman in profile with natural hair, wearing a gold crown, against a starry purple sky"></div>
      </div>
    </section>
  </main>
</body>
</html>
```